Premium Juice and Wine Bottle Label

We require a premium label design for a Burgundy style wine bottle - the design should reflect pure and organic theme, with a reference to New Zealand blueberries. The winning design will look high-end, simple but sophisticated. Our logo is attached, refer :

https://www.orvalecellars.co.nz and https://www.pirovane.co.nz/wines/details/coming-soon-showcase/2018

for inspiration.

Target Market(s)

High-end retail grocery stores, wine shops, bars.

Requirements
Must have
• Label should leave enough space for barcode and nutrients/ingredients etc. Reference to New Zealand, natural-beverage, be very high-end in design. Refer links in project description for inspiration. Refer to attached logo, which must be used - feel free to change colour in order to obtain the best high-class design.
Nice to have
• N/A.
Should not have
• Cartoons or pictures of berries.

```html
<!DOCTYPE html>
<html lang="en">
<head>
<meta charset="utf-8">
<title>Kerrow Lane Pinot Noir Label</title>
<link rel="stylesheet" href="https://fonts.googleapis.com/css2?family=Montserrat:wght@400;500;600&family=Yellowtail&display=swap">
<style>
  :root {
    --navy: #15243a;
    --paper: #fbfbfa;
    --gold-light: #f3c75a;
    --gold: #e3a12c;
    --gold-deep: #c2651c;
    --sketch: #e6e8ec;
  }
  * { margin: 0; padding: 0; box-sizing: border-box; }
  html, body { width: 1200px; height: 860px; overflow: hidden; }
  body {
    background: var(--navy);
    display: flex; align-items: center; justify-content: center;
    font-family: "Montserrat", sans-serif;
  }
  .label {
    position: relative;
    width: 900px; height: 600px;
    background: var(--paper);
    overflow: hidden;
  }
  .label__frame { position: absolute; inset: 0; }
  .brand-block {
    position: absolute; left: 70px; top: 60px;
    width: 300px; height: 300px;
    background: linear-gradient(135deg, var(--gold-light) 0%, var(--gold) 45%, var(--gold-deep) 100%);
    display: flex; align-items: center; justify-content: center;
  }
  .brand-name {
    color: var(--paper);
    font-weight: 600; font-size: 40px; letter-spacing: 1px;
    text-align: center; line-height: 1.1;
  }
  .landscape-sketch {
    position: absolute; right: 40px; top: 170px;
    width: 420px; height: 300px;
    background: radial-gradient(ellipse at center, var(--sketch) 0%, rgba(230,232,236,0) 70%);
  }
  .wine-name {
    position: absolute; left: 420px; top: 120px;
    font-family: "Yellowtail", cursive;
    font-size: 150px; line-height: 1;
    background: linear-gradient(90deg, var(--gold-deep), var(--gold), var(--gold-light));
    -webkit-background-clip: text; background-clip: text; color: transparent;
  }
  .varietal {
    position: absolute; left: 470px; top: 310px; width: 330px;
    border-top: 2px solid var(--gold); border-bottom: 2px solid var(--gold);
    padding: 8px 0;
    color: var(--gold); font-size: 24px; letter-spacing: 6px; text-align: center;
  }
  .vintage {
    position: absolute; left: 470px; top: 370px; width: 330px;
    color: var(--gold); font-size: 40px; font-weight: 400; text-align: center; letter-spacing: 2px;
  }
  .origin-band { position: absolute; left: 0; bottom: 0; width: 900px; height: 150px; }
  .origin-text {
    position: absolute; left: 70px; bottom: 28px;
    color: var(--gold-light); font-size: 14px; font-weight: 500; letter-spacing: 1.5px; line-height: 1.6;
  }
  .origin-text .small { font-size: 11px; }
</style>
</head>
<body>
  <main class="label">
    <svg class="label__frame" width="900" height="600" viewBox="0 0 900 600" aria-hidden="true">
      <path d="M30 600 A520 520 0 0 1 520 20" fill="none" stroke="var(--gold)" stroke-width="2"/>
      <path d="M42 600 A510 510 0 0 1 530 32" fill="none" stroke="var(--gold)" stroke-width="1"/>
    </svg>

    <div class="landscape-sketch" role="img" aria-label="Faint line sketch of New Zealand mountain peaks"></div>

    <div class="brand-block">
      <span class="brand-name">Kerrow<br>Lane</span>
    </div>

    <h1 class="wine-name">Name</h1>
    <p class="varietal">PINOT NOIR</p>
    <p class="vintage">2018</p>

    <svg class="origin-band" viewBox="0 0 900 150" preserveAspectRatio="none" aria-hidden="true">
      <defs>
        <linearGradient id="bandGold" x1="0" y1="1" x2="1" y2="0">
          <stop offset="0" stop-color="var(--gold-deep)"/>
          <stop offset="0.5" stop-color="var(--gold)"/>
          <stop offset="1" stop-color="var(--gold-light)"/>
        </linearGradient>
      </defs>
      <path d="M0 70 L60 40 L120 55 L200 15 L270 45 L340 30 L420 60 L520 25 L600 50 L700 20 L780 45 L900 30 L900 150 L0 150 Z" fill="url(#bandGold)"/>
    </svg>
    <p class="origin-text">LOREM IPSUM<br><span class="small">WINE of NEW ZEALAND</span></p>
  </main>
</body>
</html>
```